New Flyer Design Project for phone case sales website

we need a double sided flyer to include with orders from one business to promote another new new business. These flyers are to promote our new business that sells mobile phone cases for Velmora and uTalon models. The url for the new site is www.lanternpouch.co.uk.

Target Market(s)

Anybody with a phone

Requirements
Must have
• I like the idea to have the back of the flyer portrait with a black background. I would like the outline of any velmora or utalon with our logo in the middle. I would also like our url underneath this. Can we have the wording on the front something like.
Thank you very much for your order on Fern Nook. We have teamed up with Fern Nook to offer a 10% discount on any order placed on our website. We offer phone cases to suit all uTalon and Velmora models. Why don't you check out our range? Simply enter FERNNOOK during checkout to apply your discount.
Nice to have
• Although the back will be black, the front does not necessarily need to be.

Flyer size is A6.

```html
<!DOCTYPE html>
<html lang="en">
<head>
<meta charset="utf-8">
<title>Lantern Pouch – A6 Flyer, Back and Front</title>
<link rel="stylesheet" href="https://fonts.googleapis.com/css2?family=Montserrat:wght@700&family=Open+Sans:wght@400;600;700&family=Titillium+Web:wght@700;900&display=swap">
<style>
  :root {
    --stage: #e9eef0;
    --ink-black: #151515;
    --ink-white: #ffffff;
    --muted-white: #d6d6d6;
    --accent-blue: #2437e8;
    --accent-red: #f0264f;
    --front-deep: #1a0306;
    --front-red: #a5121a;
    --front-glow: #d8261f;
    --offer-blue: #29a8e8;
    --offer-yellow: #ffd21a;
    --offer-orange: #f7941d;
    --ring-gold: #e7a52e;
  }
  * { box-sizing: border-box; margin: 0; padding: 0; }
  html, body { width: 1200px; height: 900px; overflow: hidden; }
  body { background: var(--stage); position: relative; font-family: "Open Sans", sans-serif; }

  .flyer {
    position: absolute;
    top: 100px;
    width: 495px;
    height: 700px;
    overflow: hidden;
    box-shadow: 0 10px 30px rgba(0,0,0,.18);
  }

  .brand-lockup {
    position: absolute; left: 0; right: 0;
    display: flex; align-items: center; justify-content: center; gap: 12px;
  }
  .brand-mark { background: var(--ink-white); flex: none; }
  .brand-name {
    font-family: "Montserrat", sans-serif;
    font-weight: 700;
    letter-spacing: 1px;
    color: var(--ink-white);
    white-space: nowrap;
  }

  /* Back side */
  .flyer--back { left: 80px; background: var(--ink-black); color: var(--ink-white); }
  .back-corner {
    position: absolute; top: 0; left: 0; width: 190px; height: 140px;
    background: linear-gradient(135deg, var(--accent-blue) 0%, var(--accent-red) 55%, transparent 100%);
    opacity: .85;
  }
  .flyer--back .brand-lockup { top: 250px; }
  .flyer--back .brand-mark { width: 22px; height: 22px; }
  .flyer--back .brand-name { font-size: 30px; }
  .back-copy {
    position: absolute; top: 305px; left: 100px; right: 100px;
    font-size: 11px; line-height: 1.45; text-align: center; color: var(--muted-white);
  }
  .back-cases {
    position: absolute; top: 372px; left: 160px; width: 175px; height: 135px;
    background: linear-gradient(90deg, #2c4fd8 0 48%, transparent 48% 52%, #b3161c 52%);
    border-radius: 10px;
  }
  .visit-label {
    position: absolute; top: 560px; left: 0; right: 0;
    text-align: center; font-weight: 700; font-size: 17px;
  }
  .visit-url {
    position: absolute; top: 585px; left: 0; right: 0;
    text-align: center; font-size: 17px;
  }

  /* Front side */
  .flyer--front {
    left: 625px;
    background:
      radial-gradient(ellipse 70% 45% at 50% 58%, var(--front-glow), var(--front-red) 45%, var(--front-deep) 100%);
    color: var(--ink-white);
  }
  .front-beam {
    position: absolute; top: 0; left: 150px; width: 170px; height: 260px;
    background: linear-gradient(180deg, rgba(255,255,255,.3), rgba(255,255,255,0));
  }
  .flyer--front .brand-lockup { top: 180px; }
  .flyer--front .brand-mark { width: 18px; height: 18px; }
  .flyer--front .brand-name { font-size: 23px; }
  .offer-ring { position: absolute; top: 245px; left: 82px; width: 330px; height: 330px; }
  .offer-lead {
    position: absolute; top: 318px; left: 0; right: 0; text-align: center;
    font-weight: 700; font-size: 20px; color: var(--offer-blue);
  }
  .offer-figure-row {
    position: absolute; top: 345px; left: 0; right: 0;
    display: flex; justify-content: center; align-items: flex-start; gap: 6px;
  }
  .offer-figure {
    font-family: "Titillium Web", sans-serif; font-weight: 900; font-size: 66px; line-height: 1;
    color: var(--offer-yellow);
  }
  .offer-word {
    margin-top: 8px;
    font-family: "Titillium Web", sans-serif; font-weight: 700; font-size: 18px; color: var(--offer-orange);
  }
  .offer-note {
    position: absolute; top: 418px; left: 0; right: 0; text-align: center;
    font-size: 10px; color: var(--offer-orange);
  }
  .front-url {
    position: absolute; top: 438px; left: 0; right: 0; text-align: center;
    font-size: 14px; font-weight: 600;
  }
  .front-cases {
    position: absolute; bottom: 30px; left: 95px; width: 305px; height: 130px;
    background: linear-gradient(90deg, #2a2a2a 0 18%, #d86a1e 18% 38%, #e8237a 38% 60%, #6e7a70 60% 80%, #3653c9 80%);
    border-radius: 10px;
  }
</style>
</head>
<body>

<section class="flyer flyer--back" aria-label="Flyer back">
  <div class="back-corner" role="img" aria-label="Decorative corner of angled colour stripes"></div>
  <div class="brand-lockup">
    <span class="brand-mark" aria-hidden="true"></span>
    <h1 class="brand-name">LANTERN POUCH</h1>
  </div>
  <p class="back-copy">We offer phone cases to suit all uTalon and Velmora models. Why don't you check out our range? Simply enter FERNNOOK during checkout to apply your discount.</p>
  <div class="back-cases" role="img" aria-label="Photo of a blue ring-grip phone case and a red textured phone case"></div>
  <p class="visit-label">Visit Us:</p>
  <p class="visit-url">www.lanternpouch.co.uk</p>
</section>

<section class="flyer flyer--front" aria-label="Flyer front">
  <div class="front-beam" role="img" aria-label="Soft spotlight beam"></div>
  <div class="brand-lockup">
    <span class="brand-mark" aria-hidden="true"></span>
    <h1 class="brand-name">LANTERN POUCH</h1>
  </div>
  <svg class="offer-ring" viewBox="0 0 330 330" aria-hidden="true">
    <circle cx="165" cy="165" r="150" fill="none" stroke="var(--ring-gold)" stroke-width="2" opacity=".7"/>
  </svg>
  <p class="offer-lead">Fern Nook to offer a</p>
  <div class="offer-figure-row">
    <span class="offer-figure">10%</span>
    <span class="offer-word">discount</span>
  </div>
  <p class="offer-note">on any order placed on our website</p>
  <p class="front-url">www.lanternpouch.co.uk</p>
  <div class="front-cases" role="img" aria-label="Photo of a row of phone cases in black, orange, pink, grey and blue"></div>
</section>

</body>
</html>
```